Half page (a5) ad for a company

I need a design for an ad for a company to be published in a conference catalogue. Please find enclosed the logo for a company. The company is providing health screening services. Ad should be subtle and minimalistic, i.e. logo in the centre and a phrase saying: "Be in charge of your own health" and the website bluefern.co.uk. Also please find enclosed guidlines for colours and fonts to be used.

```html
<!DOCTYPE html>
<html lang="en">
<head>
<meta charset="utf-8">
<title>Blue Fern Private – Half Page Ad</title>
<link rel="stylesheet" href="https://fonts.googleapis.com/css2?family=Montserrat:wght@300;400;700&display=swap">
<style>
  :root {
    --board: #404040;
    --red: #e31e26;
    --ink-dark: #070909;
    --paper: #ffffff;
    --ink-light: #ffffff;
    --ink-black: #111111;
  }
  * { margin: 0; padding: 0; box-sizing: border-box; }
  html, body { width: 1200px; height: 896px; overflow: hidden; }
  body {
    background: var(--board);
    font-family: "Montserrat", Arial, sans-serif;
    position: relative;
  }
  .ad {
    position: absolute;
    top: 91px;
    width: 492px;
    height: 699px;
  }
  .ad--dark { left: 82px; background: var(--ink-dark); color: var(--ink-light); }
  .ad--light { left: 615px; background: var(--paper); color: var(--ink-black); }

  .ad__frame { position: absolute; inset: 0; width: 492px; height: 699px; }
  .ad__frame path { fill: none; stroke: var(--red); stroke-width: 1; }

  .headline { position: absolute; left: 77px; top: 70px; }
  .headline__lead {
    display: block;
    color: var(--red);
    font-weight: 700;
    font-size: 44px;
    line-height: 44px;
    letter-spacing: -0.5px;
  }
  .headline__rest {
    display: block;
    font-weight: 300;
    font-size: 47px;
    line-height: 51px;
    margin-top: 6px;
    letter-spacing: 0.6px;
    white-space: nowrap;
  }

  .brand {
    position: absolute;
    left: 0; right: 0;
    top: 305px;
    text-align: center;
  }
  .brand__dot {
    display: block;
    width: 62px; height: 62px;
    margin: 0 auto 34px;
    border-radius: 50%;
    background: var(--red);
  }
  .brand__name {
    color: var(--red);
    font-weight: 400;
    font-size: 32px;
    line-height: 38px;
    letter-spacing: 0.3px;
  }

  .ad__url {
    position: absolute;
    left: 0; right: 0;
    top: 607px;
    text-align: center;
    font-weight: 400;
    font-size: 17px;
    line-height: 22px;
    letter-spacing: 0.2px;
  }
</style>
</head>
<body>

  <section class="ad ad--dark">
    <svg class="ad__frame" viewBox="0 0 492 699" aria-hidden="true">
      <path d="M144.5 80.5 H413.5 V158"/>
      <path d="M413.5 235 V619.5 H319"/>
      <path d="M177 619.5 H79.5 V242"/>
    </svg>
    <h1 class="headline">
      <span class="headline__lead">Be</span>
      <span class="headline__rest">in charge of<br>your own health</span>
    </h1>
    <div class="brand">
      <span class="brand__dot"></span>
      <p class="brand__name">Blue Fern Private</p>
    </div>
    <p class="ad__url">bluefern.co.uk</p>
  </section>

  <section class="ad ad--light">
    <svg class="ad__frame" viewBox="0 0 492 699" aria-hidden="true">
      <path d="M144.5 80.5 H413.5 V158"/>
      <path d="M413.5 235 V619.5 H319"/>
      <path d="M177 619.5 H79.5 V242"/>
    </svg>
    <h1 class="headline">
      <span class="headline__lead">Be</span>
      <span class="headline__rest">in charge of<br>your own health</span>
    </h1>
    <div class="brand">
      <span class="brand__dot"></span>
      <p class="brand__name">Blue Fern Private</p>
    </div>
    <p class="ad__url">bluefern.co.uk</p>
  </section>

</body>
</html>
```